依頼詳細
【サイトマップ】
TOPページ
---HOME
---COMPANY (会社概要/会社沿革)
---BUSINESS (事業内容)
---RECRUIT  (採用情報)
---CONTACT  (問い合わせ)
---NEWS  (新着情報)
【サイト作成においてのポイント】
・レスポンシブデザインでお願いいたします。
・各所の素材は全てURLをお送り下さい。

【イメージ全体配置構図(いれていただきたい要素)】

ワイヤーフレームをご確認ください。
①~⑧までワイヤーフレーム内にふった番号順に詳細を記載しております。

※ワイヤーフレームはあくまでも入れたい要素を並べた一例になります。
各配置、表示位置は変えていただいても問題ございません。
------------------------

①グローバルナビ
配置は上部でお願いいたします。位置は中央を希望いたします。
------

②メインビジュアル
メインビジュアルは動画(アニメーション)挿入の仕様想定で作成して頂きたいです。
参考サイト:http://www.kovtel-sample.com/
http://info.harumiwave-sample.jp/

1ページまるごと動画(アニメーション)仕様でも問題ございません。
参考サイト:http://www.quistfold-sample.com/

(こちらでは素材を用意しておりません。確認後、購入手続きをさせていただきますのでURLをお送りください)
サイズはどのデバイスでも横幅が100%になるように考えております。
縦幅はお任せしますので、素材にあわせていただけますと幸いです。
------

③新着情報
新着情報は3つ以上いれていただけますと幸いです
いれていただきたい要素は
・更新日時(年,月,日)
・更新内容のテキスト部分 20文字前後

各テキストの配置箇所、文字色、フォント、文字やボタンのサイズ、幅感等の指定はございません。
ワイヤーフレームにはいれていただきたい要素だけならべています。
------

④事業紹介箇所
入れていただきたい要素は以下になります。
・事業紹介イメージ素材
メイン動画がヘッダー部分のみに表示の場合
背景画像として、サイズは横が100%になるように考えております。
メイン動画が全体の場合
イメージ素材が浮き上がってくるようなアニメーション仕様で考えておりますので、その仕様にあったサイズ、表示方法にしていただけますと幸いです。

極力どのデバイスサイズでもバランスよく見えるような素材をご使用いただけますと幸いです。

・事業内容の名前
(Internet media、Promotion、Influencer Marketing)
・以下テキスト
(MiraKestelはインターネットを軸とした事業を展開しております。)
・下層ページへのリンクボタン

------

⑤入れていただきたい要素は以下になります。
・背景素材
メイン動画がヘッダー部分のみに表示の場合
メイン動画が全体の場合

・遷移先の中に含まれる内容の紹介
(Staff Interview、One Day、Blog)
・以下テキスト
(MiraKestelの福利厚生や、メンバーの1日の勤務スケジュールを公開)
・下層ページへのリンクボタン

------

⑥入れていただきたい要素は以下になります。
・背景素材
メイン動画がヘッダー部分のみに表示の場合
メイン動画が全体の場合

・遷移先の中に含まれる内容の紹介
(overview/ history、Greeting)
・以下テキスト
(会社概要・沿革・代表挨拶)
・下層ページへのリンクボタン

------

⑦フッター
サイト案内
------

⑧会社情報、ロゴ

以上になります。

ご不明点等がございましたらお気軽にお問い合わせ下さい。
何卒よろしくお願い申し上げます。
ページ数
1ページ
希望イメージ
• +5 0 +5
• シンプル
複雑
• 単色
カラフル
• 暗い
明るい
• 日常
高級
• 遊び心
厳粛
• 未来的
伝統的
• 女性的
男性的
希望する色
青系、水色系、グレー系、紫系
納品ファイル
• フォトショップ形式 (.psd)
補足説明
SD又は、FireworksPNGデータ
動画に関しましてはデータ添付またはURLをお送りいただけますと幸いです。
依頼公開後の追記内容
もう少し様々な作品を拝見させていただきたく、延長させていただきました。
引き続き、何卒よろしくお願いいたします。
■ 選んだ理由

全体の雰囲気が1番理想とするものに近く、構図も綺麗なバランスで組み立てられていました。
コーポレートサイトとしてシンプルかつおしゃれ見やすいものに仕上がると思い、korubin様の作品を選ばせていただきました。

■ 提案者全員のお礼・コメント

各ランサー様
この度は弊社へのコンペへご参加いただき、誠にありがとうございました。
どの作品も大変素晴らしく、当選させていただきたいアイディア、デザインがたくさんありました。
また機会がございましたら、作品をご投稿下さいますと幸いに存じます。
誠にありがとうございました。

```html
<!DOCTYPE html>
<html lang="ja">
<head>
<meta charset="utf-8">
<title>MiraKestel</title>
<link href="https://fonts.googleapis.com/css2?family=Lato:wght@300;400;700&family=Noto+Sans+JP:wght@300;400;500&display=swap" rel="stylesheet">
<style>
:root{
  --blue:#1f9fc6;
  --teal:#2aa7c2;
  --sky:#a9dbea;
  --page:#ececec;
  --white:#ffffff;
  --ink:#4a4f55;
  --muted:#8a9096;
  --photo-a:#6f7a86;
  --photo-b:#c9cfd6;
}
*{box-sizing:border-box;margin:0;padding:0}
html,body{width:1200px;height:2380px;overflow:hidden}
body{background:var(--page);font-family:"Noto Sans JP",sans-serif;color:var(--ink);position:relative}
.abs{position:absolute}
.photo{position:absolute;background:linear-gradient(135deg,var(--photo-a),var(--photo-b))}
.header{top:0;left:0;width:1200px;height:48px;background:var(--white);display:flex;align-items:center;z-index:3}
.logo{position:absolute;left:292px;top:14px;display:flex;align-items:center;gap:8px;font-family:"Lato",sans-serif;font-size:15px;color:var(--blue);font-weight:400}
.logo i{width:12px;height:12px;border-radius:50%;background:var(--blue);display:block}
.nav{position:absolute;left:492px;top:17px;display:flex;gap:80px;font-family:"Lato",sans-serif;font-size:11px;letter-spacing:.12em;color:var(--blue)}
.hero{top:48px;left:0;width:1200px;height:560px;background:linear-gradient(160deg,#5d6874,#aab3bd 55%,#7e8892)}
.welcome{top:612px;left:200px;width:800px;height:84px;background:var(--white);text-align:center;padding-top:14px;z-index:2}
.welcome h1{font-family:"Lato",sans-serif;font-weight:400;font-size:19px;color:var(--blue)}
.welcome p{font-size:10px;color:var(--blue);line-height:1.7;margin-top:10px;padding:0 24px;text-align:left}
.sky{position:absolute;background:var(--sky)}
.news{top:720px;left:208px;width:784px;display:flex;gap:14px;z-index:2}
.card{width:185px;background:var(--white);height:250px;position:relative}
.card .thumb{position:relative;height:130px}
.card .date{font-family:"Lato",sans-serif;font-size:10px;color:var(--blue);padding:12px 12px 6px}
.card p{font-size:10px;line-height:1.7;padding:0 12px;color:var(--ink)}
.card .tick{position:absolute;right:6px;bottom:6px;width:8px;height:8px;background:var(--teal)}
.panel{position:absolute;background:var(--white);padding:26px 28px;z-index:2}
.panel h2{font-family:"Lato",sans-serif;font-weight:400;font-size:26px;letter-spacing:.08em;color:var(--blue)}
.panel ul{list-style:none;margin-top:8px;font-family:"Lato",sans-serif;font-weight:300;font-size:17px;color:var(--blue);line-height:1.3}
.panel p{font-size:10px;margin-top:14px;color:var(--ink)}
.more{display:block;margin-top:16px;width:180px;height:24px;background:var(--blue);color:var(--white);font-family:"Lato",sans-serif;font-size:10px;letter-spacing:.1em;text-align:center;line-height:24px}
.sq{position:absolute;background:var(--teal);z-index:3}
.sq.light{background:var(--sky)}
.footer{top:2200px;left:0;width:1200px;height:180px;background:var(--white)}
.fcol{position:absolute;top:36px;font-size:9px;line-height:2.2;color:var(--ink)}
.copy{position:absolute;bottom:0;left:0;width:1200px;height:34px;border-top:1px solid #dcdcdc;text-align:center;line-height:34px;font-family:"Lato",sans-serif;font-size:9px;color:var(--muted)}
</style>
</head>
<body>
<header class="header abs">
  <div class="logo"><i></i>MiraKestel</div>
  <nav class="nav"><span>BUSINESS</span><span>RECRUIT</span><span>COMPANY</span><span>CONTACT</span></nav>
</header>

<div class="photo hero" role="img" aria-label="オフィスで働くスタッフの動画ビジュアル"></div>

<section class="welcome abs">
  <h1>Welcome to Advertising</h1>
  <p>株式会社MiraKestelはインターネットを軸とした事業を展開しております。メディア運営、プロモーション、インフルエンサーマーケティングを通じて、お客様の価値ある情報を多くの方へお届けします。</p>
</section>

<div class="sky" style="left:600px;top:700px;width:600px;height:290px"></div>
<section class="news abs">
  <article class="card"><div class="photo thumb" role="img" aria-label="会議の様子"></div><div class="date">2018.04.10 新着情報</div><p>新しいメディアサイトを公開いたしました。ぜひご覧ください。</p><span class="tick"></span></article>
  <article class="card"><div class="photo thumb" role="img" aria-label="打ち合わせの様子"></div><div class="date">2018.04.02 新着情報</div><p>新卒採用の募集を開始いたしました。皆様のご応募をお待ちしております。</p><span class="tick"></span></article>
  <article class="card"><div class="photo thumb" role="img" aria-label="チームの写真"></div><div class="date">2018.03.20 新着情報</div><p>スタッフインタビューを更新いたしました。</p><span class="tick"></span></article>
  <article class="card"><div class="photo thumb" role="img" aria-label="オフィス風景"></div><div class="date">2018.03.05 新着情報</div><p>オフィスを移転いたしました。今後ともよろしくお願いいたします。</p><span class="tick"></span></article>
</section>

<div class="sky" style="left:290px;top:1000px;width:910px;height:320px"></div>
<div class="photo" style="left:480px;top:1000px;width:520px;height:280px;z-index:1" role="img" aria-label="木製の社名サインのある受付"></div>
<span class="sq" style="left:470px;top:1030px;width:40px;height:40px"></span>
<span class="sq light" style="left:440px;top:1060px;width:30px;height:30px"></span>
<section class="panel" style="left:190px;top:1070px;width:360px;height:220px">
  <h2>BUSINESS</h2>
  <ul><li>Internet Media</li><li>Promotion</li><li>Influencer Marketing</li></ul>
  <p>MiraKestelはインターネットを軸とした事業を展開しております。</p>
  <span class="more">MORE</span>
</section>

<div class="sky" style="left:0;top:1330px;width:920px;height:300px"></div>
<div class="photo" style="left:190px;top:1340px;width:530px;height:300px;z-index:1" role="img" aria-label="明るいオフィスフロア"></div>
<span class="sq" style="left:680px;top:1350px;width:40px;height:40px"></span>
<span class="sq light" style="left:720px;top:1380px;width:30px;height:30px"></span>
<section class="panel" style="left:660px;top:1390px;width:350px;height:210px">
  <h2>RECRUIT</h2>
  <ul><li>Staff Interview</li><li>One Day</li><li>Blog</li></ul>
  <p>MiraKestelの福利厚生や、メンバーの1日の勤務スケジュールを公開</p>
  <span class="more">MORE</span>
</section>

<div class="sky" style="left:200px;top:1680px;width:1000px;height:500px"></div>
<div class="photo" style="left:500px;top:1740px;width:500px;height:320px;z-index:1" role="img" aria-label="社名サインのあるエントランス"></div>
<span class="sq" style="left:470px;top:1890px;width:40px;height:40px"></span>
<span class="sq light" style="left:440px;top:1920px;width:30px;height:30px"></span>
<section class="panel" style="left:190px;top:1920px;width:360px;height:220px">
  <h2>COMPANY</h2>
  <ul><li>Overview/History</li><li>Greeting</li></ul>
  <p>会社概要・沿革・代表挨拶</p>
  <span class="more">MORE</span>
</section>

<footer class="footer abs">
  <div class="fcol" style="left:240px">COMPANY 会社概要<br>会社沿革<br>代表挨拶<br>BUSINESS 事業内容</div>
  <div class="fcol" style="left:370px">RECRUIT 採用情報<br>スタッフインタビュー<br>ブログ</div>
  <div class="fcol" style="left:490px">CONTACT 問い合わせ<br>NEWS 新着情報</div>
  <div class="logo" style="left:640px;top:36px"><i></i>MiraKestel</div>
  <div class="fcol" style="left:780px">株式会社MiraKestel<br>〒000-0000 東京都サンプル区1-2-3<br>TEL 00-0000-0000</div>
  <div class="copy">Copyright © MiraKestel All Rights Reserved.</div>
</footer>
</body>
</html>
```